Postcard for Dental Lab to Dental Lab

We are a wholesale Outsourcing Dental Lab. We are looking for a postcard design that will attract new customers and accounts. We market to Only other dental Labs. We are looking for a design based around "new year resolutions list for a dental lab" Our logo colors are green, gold and white. We want a box with a check mark in it showing that our lab has meet all of the new year resolution lists.

We are looking for a new years resolutions postcard. It should have a professional look as we are sending it to dental Labs.

Maybe something that shows a fresh start and new year. The main focus point would be a "New years resolution" List. This list should look like it has been written on paper. It should list things like
The heading should read. "New Years Resolutions list"
1. Work less Hours while maintaining current income
2. Expand current dental Lab
3. Make More money with Less headaches.
4. Gain more freedom from long hours behind bench.

Then another heading: "Ways to achieve resolutions list"
"Find outsourcing dental lab that offers..."

1. Find a experienced full service dental Lab

2. Lab that is FDA and KTRC certified.

3. Competitive prices.

4. Has consistent quality restorations and products.

5. BRIVEN WORKS
That was easy.

On the back of the card we would like some bullet points.
1. ISO 9001, 13485 and FDA Certified.
2. Restorative Goods Quality Review Scheme (RGQRS) certified.
3. 5 year warranty on fixed and 2 years on removable.
4. Local Customer service in Phoenix Arizona assigned to your office and cases.
5. Higher productivity- Allows you to provide more units from your lab with the same number of technicians.

Here are two customer quotes that we can use.
"Impressive work....Better than what we can do locally!..."

"Thanks for your wonderful service, our business is increasing by 20% per month..."

Please have and area for the mailing address and return address. We are looking for a headline that is large on the front of the post card that will grab attention. Maybe an image of sparklers or fireworks or something with a new years new start.
Keep the designs coming as we are really needing to get this design finished quick.
Thanks!

I have uploaded a sample of what we are looking for. This is from a diffrent dental lab but with the same idea. Please look at this design but include what we have asked for. thank you
Updates

This flyer will be 6” x 11” with an eye catching basic design on the front and some more detailed info on the back.  I would like to focus on getting a great front design and then we can work on making the back coordinate.  Can have some brighter colors for the “New Year’s Resolution” part (look festive and eye catching) Maybe some Fireworks in the background

This flyer will be an introduction to our business in new areas that we have not worked in before. 
The concept is to introduce our lab, let them know we will be offering our services in their regions and do it in a creative, eye catching way. 

The concept I would like for the flyer is a new year’s resolution list that has a list of things they need to complete their goals.  The list is needs to look like a piece of paper with a visually appealing header of “NEW YEAR’S RESOLUTION” and a hand written look of the rest of what is below. The bullet points need to be boxes and they need check marks in them like they put a check mark in the boxes by hand.

On the front of the postcard there needs to be a place for our phone number 855-314-9087 and then an area to place "Special Trial offer" 5 free PFM'S!

Reason: I would like to provide more feed back. Due to the holiday we will be extending the deadline. Thank you for the designs please keep them coming.

Reason: Still looking for a good design. please keep them coming. Thank you

Target Market(s)

Dental LAB OWNERS.

Industry/Entity Type

Dental

Requirements
Must have
• New Year resolutions theme. Looking for a list that is written on a piece of paper with checkboxes next to every one of the lists.

```html
<!DOCTYPE html>
<html lang="en">
<head>
<meta charset="utf-8">
<title>Briven Works – New Year's Resolutions Postcard</title>
<link rel="stylesheet" href="https://fonts.googleapis.com/css2?family=Mystery+Quest&family=Gochi+Hand&display=swap">
<style>
  :root {
    --backdrop: #e6e6e6;
    --night-deep: #0f2556;
    --night-mid: #1d3f86;
    --night-light: #2c5cab;
    --paper-edge: #b8945a;
    --ribbon: #e2291f;
    --ribbon-dark: #a8160f;
    --ribbon-gold: #e9b44a;
    --ink: #2a2622;
    --ink-soft: #4f4335;
    --snow: #ffffff;
    --snow-shade: #dfe6ee;
    --white: #ffffff;
    --brand-green: #2f8a3c;
    --bell-gold: #e0a83a;
    --bell-deep: #b77a1c;
    --holly-green: #6fb33a;
    --pine-green: #1f8a2c;
  }
  * { box-sizing: border-box; margin: 0; padding: 0; }
  html, body { width: 1200px; height: 900px; overflow: hidden; }
  body { background: var(--backdrop); position: relative; font-family: "Gochi Hand", cursive; }

  .postcard {
    position: absolute; left: 370px; top: 28px;
    width: 460px; height: 844px; overflow: hidden;
    background: radial-gradient(ellipse at 30% 15%, var(--night-light), var(--night-mid) 45%, var(--night-deep));
    box-shadow: 0 6px 18px rgba(0,0,0,.18);
  }
  .postcard > * { position: absolute; }

  .star-field, .parchment, .snowfield { left: 0; top: 0; width: 460px; height: 844px; }

  .year {
    left: 30px; top: 30px;
    font-family: "Mystery Quest", cursive;
    font-size: 86px; line-height: 1; color: var(--white); letter-spacing: 4px;
    text-shadow: 0 2px 4px rgba(0,0,0,.35);
  }

  .illustration { border-radius: 18px; }

  .bells-art {
    left: 250px; top: 8px; width: 150px; height: 140px;
    background: linear-gradient(160deg, var(--ribbon) 0%, var(--bell-gold) 38%, var(--bell-deep) 100%);
  }

  .ribbon { left: 0; width: 460px; height: 110px; }
  .ribbon-top { top: 158px; }
  .ribbon-bottom { top: 402px; }
  .ribbon-title {
    left: 0; width: 460px; text-align: center; font-weight: 400;
    font-family: "Mystery Quest", cursive; font-size: 24px; color: var(--ink);
    line-height: 1; white-space: nowrap;
  }
  .ribbon-top-title { top: 203px; transform: rotate(-1.5deg); }
  .ribbon-bottom-title { top: 446px; font-size: 22px; transform: rotate(-1.5deg); }

  .wreath-art {
    left: 34px; top: 244px; width: 124px; height: 150px;
    background: linear-gradient(180deg, var(--holly-green) 0%, #4f9a2a 70%, var(--ribbon-dark) 100%);
  }

  .brand-tag {
    left: 4px; top: 330px; height: 40px; padding: 0 10px 0 6px;
    display: flex; align-items: center; gap: 6px;
    background: var(--white);
    font-family: "Gochi Hand", cursive; font-size: 17px; color: var(--brand-green);
  }
  .brand-dot { width: 20px; height: 20px; border-radius: 50%; background: var(--brand-green); }

  .resolution-list, .method-list { list-style: none; }
  .resolution-list { left: 200px; top: 272px; width: 230px; }
  .resolution-list li {
    display: flex; align-items: center; justify-content: flex-end; gap: 6px;
    text-align: right; font-size: 13px; line-height: 1.05; color: var(--ink-soft); height: 32px;
  }
  .method-list { left: 136px; top: 522px; width: 212px; }
  .method-list li {
    display: flex; align-items: center; gap: 8px;
    font-size: 12.5px; line-height: 1.05; color: var(--ink-soft); height: 30px;
  }
  .tick-box { flex: none; width: 26px; height: 26px; }

  .tree-art {
    left: 354px; top: 540px; width: 84px; height: 150px;
    background: linear-gradient(180deg, #2a9a36 0%, var(--pine-green) 60%, #146a20 100%);
  }

  .snowman-art {
    left: 18px; top: 600px; width: 110px; height: 190px;
    background: linear-gradient(180deg, #c8302a 0%, #c8302a 26%, #f5f7fa 34%, #e9edf2 100%);
  }

  .phone-icon { left: 58px; top: 758px; width: 28px; height: 28px; }
  .phone-number {
    left: 18px; top: 800px; font-family: "Gochi Hand", cursive; font-size: 14px; color: var(--ink-soft);
    letter-spacing: .5px;
  }

  .trial-offer {
    right: 34px; top: 780px; text-align: center;
    font-family: "Mystery Quest", cursive; font-size: 19px; line-height: 1.15; color: var(--ink);
  }
</style>
</head>
<body>
<svg width="0" height="0" style="position:absolute">
  <defs>
    <symbol id="tick-box" viewBox="0 0 26 26">
      <rect x="2" y="6" width="18" height="18" fill="none" stroke="#2a2622" stroke-width="2.4"/>
      <path d="M5 14 L10 20 L24 2" fill="none" stroke="#2a2622" stroke-width="3.2" stroke-linecap="round" stroke-linejoin="round"/>
    </symbol>
  </defs>
</svg>

<article class="postcard">
  <svg class="star-field" viewBox="0 0 460 844" aria-hidden="true">
    <g fill="#ffffff">
      <circle cx="30" cy="18" r="1.6"/><circle cx="120" cy="14" r="1.2"/><circle cx="210" cy="30" r="1.8"/>
      <circle cx="250" cy="120" r="1.4"/><circle cx="18" cy="140" r="1.2"/><circle cx="440" cy="170" r="1.5"/>
      <circle cx="448" cy="320" r="1.2"/><circle cx="14" cy="470" r="1.5"/><circle cx="22" cy="560" r="1.2"/>
      <circle cx="444" cy="520" r="1.3"/><circle cx="170" cy="136" r="1.1"/>
    </g>
  </svg>

  <div class="year">2014</div>

  <svg class="parchment" viewBox="0 0 460 844" aria-hidden="true">
    <defs>
      <radialGradient id="paper" cx="50%" cy="45%" r="70%">
        <stop offset="0" stop-color="#f3e4c2"/>
        <stop offset=".7" stop-color="#e2c792"/>
        <stop offset="1" stop-color="#c9a56a"/>
      </radialGradient>
    </defs>
    <path d="M190 128 C250 112 330 108 438 104 L438 770 L40 770 L40 240 C60 200 120 150 190 128 Z" fill="url(#paper)"/>
  </svg>

  <div class="illustration bells-art" role="img" aria-label="Two golden bells tied with a red ribbon bow"></div>

  <svg class="ribbon ribbon-top" viewBox="0 0 460 110" aria-hidden="true">
    <path d="M0 30 C120 8 300 6 460 26 L460 92 C300 70 130 74 0 98 Z" fill="#a8160f"/>
    <path d="M0 34 C120 14 300 12 460 32 L460 86 C300 64 130 68 0 92 Z" fill="#e2291f"/>
    <path d="M0 38 C120 18 300 16 460 36" fill="none" stroke="#e9b44a" stroke-width="2"/>
    <path d="M0 88 C130 64 300 60 460 82" fill="none" stroke="#e9b44a" stroke-width="2"/>
  </svg>
  <h1 class="ribbon-title ribbon-top-title">NEW YEARS RESOLUTIONS LIST</h1>

  <div class="illustration wreath-art" role="img" aria-label="Green holiday wreath with red berries and a red bow"></div>
  <div class="brand-tag"><span class="brand-dot"></span>BRIVEN WORKS</div>

  <ul class="resolution-list">
    <li><span>Work less Hours while<br>maintaining current income</span><svg class="tick-box"><use href="#tick-box"/></svg></li>
    <li><span>Expand current dental Lab</span><svg class="tick-box"><use href="#tick-box"/></svg></li>
    <li><span>Make More money with<br>Less headaches</span><svg class="tick-box"><use href="#tick-box"/></svg></li>
    <li><span>Gain more freedom from<br>long hours behind bench</span><svg class="tick-box"><use href="#tick-box"/></svg></li>
  </ul>

  <svg class="ribbon ribbon-bottom" viewBox="0 0 460 110" aria-hidden="true">
    <path d="M0 24 C130 6 300 6 460 22 L460 90 C300 72 130 74 0 94 Z" fill="#a8160f"/>
    <path d="M0 28 C130 10 300 10 460 28 L460 84 C300 66 130 68 0 88 Z" fill="#e2291f"/>
    <path d="M0 32 C130 14 300 14 460 32" fill="none" stroke="#e9b44a" stroke-width="2"/>
    <path d="M0 84 C130 64 300 62 460 80" fill="none" stroke="#e9b44a" stroke-width="2"/>
  </svg>
  <h2 class="ribbon-title ribbon-bottom-title">WAYS TO ACHIEVE RESOLUTIONS LIST</h2>

  <ul class="method-list">
    <li><svg class="tick-box"><use href="#tick-box"/></svg><span>Find a experienced<br>full service dental Lab</span></li>
    <li><svg class="tick-box"><use href="#tick-box"/></svg><span>Lab that is FDA and KTRC certified</span></li>
    <li><svg class="tick-box"><use href="#tick-box"/></svg><span>Competitive prices</span></li>
    <li><svg class="tick-box"><use href="#tick-box"/></svg><span>Has consistent quality restorations<br>and products.</span></li>
    <li><svg class="tick-box"><use href="#tick-box"/></svg><span>BRIVEN WORKS</span></li>
  </ul>

  <div class="illustration tree-art" role="img" aria-label="Green Christmas tree decorated with white baubles"></div>

  <svg class="snowfield" viewBox="0 0 460 844" aria-hidden="true">
    <path d="M0 720 C90 700 150 742 240 738 C330 734 390 700 460 712 L460 844 L0 844 Z" fill="#dfe6ee"/>
    <path d="M0 732 C90 714 150 754 240 750 C330 746 390 714 460 726 L460 844 L0 844 Z" fill="#ffffff"/>
  </svg>

  <div class="illustration snowman-art" role="img" aria-label="Snowman wearing a red knitted hat and scarf"></div>

  <svg class="phone-icon" viewBox="0 0 28 28" aria-hidden="true">
    <circle cx="14" cy="14" r="13" fill="#e2291f"/>
    <path d="M10 7 L12.5 7 L13.5 11 L11.8 12.3 C12.6 14.2 13.8 15.4 15.7 16.2 L17 14.5 L21 15.5 L21 18 C21 19.2 20 20 18.8 20 C12.8 19.6 8.4 15.2 8 9.2 C8 8 8.8 7 10 7 Z" fill="#ffffff"/>
  </svg>
  <p class="phone-number">855 314 9087</p>

  <p class="trial-offer">"SPECIAL TRIAL OFFER"<br>5 FREE PFM'S!</p>
</article>
</body>
</html>
```